Inspiration Poster

Inspirational Poster that has a Kamran Dulo like abstract look (http://www.vexalo.com/images/search?q=kamran+dulo&FORM=HDRSC2) with the text:

"we walk not in order to arrive at the promise land but because walking itself is a revolution"
-Peter Ambrick

```html
<!DOCTYPE html>
<html lang="en">
<head>
<meta charset="utf-8">
<title>Inspiration Poster</title>
<link rel="stylesheet" href="https://fonts.googleapis.com/css2?family=Federo&display=swap">
<style>
  :root {
    --tone-blue: #3f5585;
    --tone-slate: #8d97a8;
    --tone-sand: #e9d3ad;
    --tone-peach: #f8dcaa;
    --text-light: rgba(255, 255, 255, 0.92);
  }
  html, body {
    margin: 0;
    padding: 0;
    width: 1200px;
    height: 751px;
    overflow: hidden;
  }
  .poster {
    position: relative;
    width: 1200px;
    height: 751px;
    overflow: hidden;
    font-family: "Federo", sans-serif;
    color: var(--text-light);
  }
  .poster__backdrop {
    position: absolute;
    inset: 0;
    background:
      radial-gradient(ellipse 380px 120px at 520px 500px, rgba(90, 110, 150, 0.35), transparent 70%),
      radial-gradient(ellipse 260px 90px at 880px 250px, rgba(150, 150, 150, 0.25), transparent 70%),
      linear-gradient(30deg, var(--tone-blue) 0%, var(--tone-slate) 40%, var(--tone-sand) 68%, var(--tone-peach) 100%);
  }
  .quote {
    position: absolute;
    left: 100px;
    top: 72px;
    margin: 0;
    font-size: 78px;
    line-height: 96px;
    font-weight: 400;
    letter-spacing: 0.5px;
  }
  .quote__line {
    display: block;
    white-space: nowrap;
  }
  .quote__line--indent {
    padding-left: 22px;
  }
  .attribution {
    position: absolute;
    left: 100px;
    top: 588px;
    margin: 0;
    font-size: 82px;
    line-height: 96px;
    font-weight: 400;
  }
</style>
</head>
<body>
  <main class="poster">
    <div class="poster__backdrop" role="img" aria-label="Soft-toned photo of water droplets shaped like two bare footprints on a pale surface"></div>
    <blockquote class="quote">
      <span class="quote__line">”We walk not in order to</span>
      <span class="quote__line">arrive at the promise land</span>
      <span class="quote__line">but because walking itself</span>
      <span class="quote__line quote__line--indent">is a Revolution”</span>
    </blockquote>
    <p class="attribution">-Peter Ambrick</p>
  </main>
</body>
</html>
```